Pull up banner design for mortgage broking firm $500 competition

Need a pull up banner design the banner will be
1.8m banner tall
Colours should be similar to our Logo blues and yellows
The logo at the top
the cloud house needs to be in the middle
the $500 needs to be big and stand out
The terms and conditions should be in dot points
the top line to be bigger than the bottom and different colour font.
Please see the attached dot point design down the bottom - but use yellow and blue colours.
the licensee details need to be in small print down the bottom.
Mortgage

```html
<!DOCTYPE html>
<html lang="en">
<head>
<meta charset="utf-8">
<title>Kindred Home Loans – Pull Up Banner</title>
<link href="https://fonts.googleapis.com/css2?family=Fjalla+One&family=Arimo:wght@400;700&family=Kalam:wght@700&display=swap" rel="stylesheet">
<style>
  :root {
    --navy: #1b4a78;
    --box-blue: #2a5e92;
    --sky: #2b8bd0;
    --gold: #f2b21f;
    --white: #ffffff;
    --photo-light: #eeeae6;
    --photo-mid: #c9b9a6;
  }
  * { margin: 0; padding: 0; box-sizing: border-box; }
  html, body { width: 1200px; height: 2699px; overflow: hidden; background: var(--white); }
  .banner { position: relative; width: 1200px; height: 2699px; overflow: hidden; background: var(--white); font-family: 'Arimo', Arial, sans-serif; }

  .top-strip { position: absolute; left: 0; top: 0; width: 1200px; height: 22px; background: var(--navy); }

  .brand { position: absolute; left: 160px; top: 62px; display: flex; align-items: center; gap: 28px; white-space: nowrap; }
  .brand-dot { width: 130px; height: 130px; border-radius: 50%; background: var(--sky); flex: none; }
  .brand-name { font-family: 'Fjalla One', 'Arial Narrow', sans-serif; font-size: 84px; line-height: 1; color: var(--navy); text-transform: uppercase; letter-spacing: 2px; }
  .tagline { position: absolute; left: 355px; top: 236px; font-family: 'Kalam', cursive; font-size: 54px; line-height: 1.1; color: var(--gold); letter-spacing: 2px; white-space: nowrap; }

  .headline { font-family: 'Fjalla One', 'Arial Narrow', sans-serif; color: var(--navy); font-weight: 400; }
  .headline span { position: absolute; white-space: nowrap; line-height: 1; }
  .headline .line-one { left: 96px; top: 368px; font-size: 100px; }
  .headline .line-two { left: 96px; top: 510px; font-size: 100px; }
  .headline .amount { left: 708px; top: 463px; font-size: 270px; color: var(--gold); transform: scaleX(0.72); transform-origin: left top; text-shadow: 7px 6px 0 var(--navy); }

  .photo { position: absolute; left: 0; top: 725px; width: 1200px; height: 905px; background: linear-gradient(160deg, var(--photo-light) 0%, #e2d8cc 45%, var(--photo-mid) 100%); }
  .wave { position: absolute; left: 0; top: 1225px; width: 1200px; height: 410px; }

  .info { position: absolute; left: 0; top: 1630px; width: 1200px; height: 765px; background: var(--navy); }
  .offer { position: absolute; left: 0; top: 122px; width: 1200px; text-align: center; font-family: 'Fjalla One', 'Arial Narrow', sans-serif; font-weight: 400; font-size: 48px; line-height: 1.2; color: var(--white); white-space: nowrap; }
  .terms-title { position: absolute; left: 0; top: 220px; width: 1200px; text-align: center; font-size: 29px; line-height: 1.2; font-weight: 700; color: var(--gold); }

  .terms { position: absolute; left: 22px; top: 264px; width: 1157px; display: grid; grid-template-columns: 565px 565px; column-gap: 27px; row-gap: 21px; list-style: none; }
  .term { display: flex; height: 82px; }
  .term-tick { width: 82px; flex: none; background: var(--box-blue); display: flex; align-items: center; justify-content: center; margin-right: 8px; }
  .term-tick svg { width: 54px; height: 54px; }
  .term-body { flex: 1; background: var(--box-blue); padding: 7px 12px 0 22px; overflow: hidden; }
  .term-head { font-size: 14px; font-weight: 700; color: var(--gold); line-height: 1.15; }
  .term-text { font-size: 14px; color: var(--white); line-height: 1.15; margin-top: 4px; }
  .term-body.solo { display: flex; align-items: center; padding-top: 0; }

  .licence { position: absolute; left: 0; top: 708px; width: 1200px; text-align: center; font-size: 14px; color: var(--white); line-height: 1.25; }

  .web-band { position: absolute; left: 0; top: 2393px; width: 1200px; height: 180px; background: var(--gold); display: flex; align-items: center; justify-content: center; }
  .web-address { font-family: 'Fjalla One', 'Arial Narrow', sans-serif; font-size: 74px; color: var(--navy); letter-spacing: 1px; white-space: nowrap; }
  .bottom-strip { position: absolute; left: 0; top: 2573px; width: 1200px; height: 126px; background: var(--navy); }
</style>
</head>
<body>
<div class="banner">
  <div class="top-strip"></div>

  <header class="brand">
    <span class="brand-dot"></span>
    <span class="brand-name">Kindred Home Loans</span>
  </header>
  <p class="tagline">here for you</p>

  <h1 class="headline">
    <span class="line-one">We give you savings</span>
    <span class="line-two">or we give you</span>
    <span class="amount">$500</span>
  </h1>

  <div class="photo" role="img" aria-label="Photo of a smiling couple relaxing on a white sofa, looking at a tablet together"></div>

  <svg class="wave" viewBox="0 0 1200 410" preserveAspectRatio="none" aria-hidden="true">
    <path d="M1200 0 C 950 200 560 330 0 330 L0 410 L1200 410 Z" fill="var(--sky)"/>
    <path d="M1200 120 C 960 320 560 400 0 372 L0 410 L1200 410 Z" fill="var(--white)"/>
    <path d="M1200 134 C 960 334 560 410 0 380 L0 410 L1200 410 Z" fill="var(--navy)"/>
  </svg>

  <section class="info">
    <h2 class="offer">Free home loan health check with a KHL lending adviser!</h2>
    <h3 class="terms-title">Terms and conditions</h3>

    <ul class="terms">
      <li class="term">
        <span class="term-tick"><svg viewBox="0 0 54 54"><circle cx="27" cy="27" r="22" fill="none" stroke="#fff" stroke-width="4"/><path d="M15 27 L25 37 L46 9" fill="none" stroke="#fff" stroke-width="6" stroke-linecap="round" stroke-linejoin="round"/></svg></span>
        <div class="term-body"><p class="term-head">Our Kindred Return policy is where the savings start</p><p class="term-text">All calculations of savings include KHL Kindred Return policy of 0.15% on the running balance of your loan.</p></div>
      </li>
      <li class="term">
        <span class="term-tick"><svg viewBox="0 0 54 54"><circle cx="27" cy="27" r="22" fill="none" stroke="#fff" stroke-width="4"/><path d="M15 27 L25 37 L46 9" fill="none" stroke="#fff" stroke-width="6" stroke-linecap="round" stroke-linejoin="round"/></svg></span>
        <div class="term-body"><p class="term-head">The client must currently reside there.</p><p class="term-text">Your current loan must be for the home you currently reside in.</p></div>
      </li>
      <li class="term">
        <span class="term-tick"><svg viewBox="0 0 54 54"><circle cx="27" cy="27" r="22" fill="none" stroke="#fff" stroke-width="4"/><path d="M15 27 L25 37 L46 9" fill="none" stroke="#fff" stroke-width="6" stroke-linecap="round" stroke-linejoin="round"/></svg></span>
        <div class="term-body"><p class="term-head">At least $300,000 loan</p><p class="term-text">Your current loan size needs to be a minimum of $300,000.</p></div>
      </li>
      <li class="term">
        <span class="term-tick"><svg viewBox="0 0 54 54"><circle cx="27" cy="27" r="22" fill="none" stroke="#fff" stroke-width="4"/><path d="M15 27 L25 37 L46 9" fill="none" stroke="#fff" stroke-width="6" stroke-linecap="round" stroke-linejoin="round"/></svg></span>
        <div class="term-body"><p class="term-head">Must be with Big 4 home loans only HBB, SCB, CNB or UBK branded home loans</p><p class="term-text">Must be a big four loan easily accessible by the public.</p></div>
      </li>
      <li class="term">
        <span class="term-tick"><svg viewBox="0 0 54 54"><circle cx="27" cy="27" r="22" fill="none" stroke="#fff" stroke-width="4"/><path d="M15 27 L25 37 L46 9" fill="none" stroke="#fff" stroke-width="6" stroke-linecap="round" stroke-linejoin="round"/></svg></span>
        <div class="term-body"><p class="term-head">Must be local and in person.</p><p class="term-text">Your appointment must be within 35km of Melbourne CBD and face-to-face with a KHL adviser.</p></div>
      </li>
      <li class="term">
        <span class="term-tick"><svg viewBox="0 0 54 54"><circle cx="27" cy="27" r="22" fill="none" stroke="#fff" stroke-width="4"/><path d="M15 27 L25 37 L46 9" fill="none" stroke="#fff" stroke-width="6" stroke-linecap="round" stroke-linejoin="round"/></svg></span>
        <div class="term-body"><p class="term-head">The loan must be at least 30 months old.</p><p class="term-text">Must be at least 30 months since day of settlement.</p></div>
      </li>
      <li class="term">
        <span class="term-tick"><svg viewBox="0 0 54 54"><circle cx="27" cy="27" r="22" fill="none" stroke="#fff" stroke-width="4"/><path d="M15 27 L25 37 L46 9" fill="none" stroke="#fff" stroke-width="6" stroke-linecap="round" stroke-linejoin="round"/></svg></span>
        <div class="term-body"><p class="term-head">Must be an owner occupied loan with a Variable Rate and principal interest repayments</p><p class="term-text">All three of the above criteria must be met (KHL specifically exclude investment loans, fixed interest and interest only loans.</p></div>
      </li>
      <li class="term">
        <span class="term-tick"><svg viewBox="0 0 54 54"><circle cx="27" cy="27" r="22" fill="none" stroke="#fff" stroke-width="4"/><path d="M15 27 L25 37 L46 9" fill="none" stroke="#fff" stroke-width="6" stroke-linecap="round" stroke-linejoin="round"/></svg></span>
        <div class="term-body solo"><p class="term-head">LVR must be 80% or less under bank valuation</p></div>
      </li>
    </ul>

    <p class="licence">A Bright Path Lending Pty Ltd Trading As Kindred Home Loans ABN 00 000 000 001,<br>Authorised Representative of Meridian Finance Network ABN 00 000 000 002, Australian Credit License 000 000.</p>
  </section>

  <footer class="web-band"><span class="web-address">www.kindredhl.com.au</span></footer>
  <div class="bottom-strip"></div>
</div>
</body>
</html>
```